Design a leaflet and business card for Tarvello Consulting

Design an A5 Double Sided Flyer / Leaflet & Double Sided Business Card for my business.

Use my logo.

The Leaflet must have my Logo, Contact Details as below and the text required.

Needs to be creative and eye catching to attract new business.

Business Card must have same design style as leaflet.

Font for our logo is MYRIAD PRO.

Text to use on the leaflet.
-------------------------------

Web Design & Development Company in Brackwell
Website Design for Businesses, Events & Organisations

We also offer:
Graphic Design
S.E.O & Marketing
Application Design

Leave Room for our address, telephone number and e-mail.

Contact Details:
7 Ashlin Grove, Brackwell, Westmere, ZX14 6JB
Tel: 01632 960215
E-Mail: info@tarvelloexample.co.uk

Must have the website URL on the leaflet. ( www.tarvelloexample.co.uk )

Facebook Icon
Twitter Icon

Colours: Pink, White, Black, Dark Gray, Yellow (The Design Must Stand Out.)

There will be alot of work for the winning designer.

```html
<!DOCTYPE html>
<html lang="en">
<head>
<meta charset="utf-8">
<title>Tarvello Consulting – Business Card</title>
<link rel="stylesheet" href="https://fonts.googleapis.com/css2?family=Open+Sans:wght@400;600;700;800&display=swap">
<style>
  :root {
    --pink: #e6137f;
    --black: #161616;
    --dark-gray: #3a3a3a;
    --mid-gray: #8a8a8a;
    --line-gray: #d4d4d4;
    --white: #ffffff;
    --backdrop: #ececec;
  }
  * { box-sizing: border-box; margin: 0; padding: 0; }
  html, body { width: 1200px; height: 823px; overflow: hidden; }
  body {
    background: var(--backdrop);
    font-family: "Open Sans", Arial, sans-serif;
    position: relative;
  }
  .card {
    position: absolute;
    top: 133px;
    width: 360px;
    height: 556px;
    background: var(--white);
    overflow: hidden;
    box-shadow: 0 6px 22px rgba(0,0,0,.18);
  }
  .card--back { left: 190px; }
  .card--front { left: 650px; }
  .card__shapes { position: absolute; inset: 0; width: 360px; height: 556px; }
  .card > *:not(.card__shapes) { position: absolute; }

  /* back side */
  .social { left: 22px; right: 22px; }
  .social__row {
    display: flex; align-items: center; gap: 10px;
    height: 38px;
    border-bottom: 1px solid var(--line-gray);
    font-size: 14px; font-weight: 700; color: var(--dark-gray);
    white-space: nowrap;
  }
  .social__mark { width: 18px; height: 18px; background: var(--dark-gray); border-radius: 3px; flex: none; }
  .tagline {
    top: 152px; left: 20px; right: 20px;
    color: var(--white); font-size: 21px; font-weight: 700; line-height: 1.28; text-align: center;
  }
  .services {
    top: 246px; left: 20px; right: 20px;
    color: var(--white); font-size: 15px; font-weight: 600; line-height: 1.35; text-align: center;
  }
  .brand { display: flex; align-items: center; gap: 10px; }
  .brand__dot { width: 22px; height: 22px; border-radius: 50%; background: var(--pink); flex: none; }
  .brand__name { font-size: 27px; font-weight: 700; color: var(--black); white-space: nowrap; }
  .card--back .brand { top: 418px; left: 0; right: 0; justify-content: center; }
  .url { bottom: 26px; left: 0; right: 0; text-align: center; color: var(--pink); font-size: 17px; font-weight: 700; }

  /* front side */
  .card--front .brand { top: 36px; left: 26px; }
  .card--front .brand__name { color: var(--white); font-size: 26px; }
  .person { top: 150px; left: 30px; right: 20px; }
  .person__name { font-size: 32px; font-weight: 800; color: var(--black); line-height: 1.1; }
  .person__role { font-size: 19px; color: var(--dark-gray); margin-top: 4px; }
  .contact { list-style: none; }
  .contact li { display: flex; align-items: center; gap: 10px; }
  .contact svg { flex: none; }
  .contact--personal { top: 250px; left: 30px; font-size: 14px; color: var(--dark-gray); }
  .contact--personal li { height: 24px; }
  .contact--company { top: 372px; left: 26px; right: 14px; font-size: 14px; font-weight: 700; color: var(--white); }
  .contact--company li { min-height: 30px; line-height: 1.25; }
</style>
</head>
<body>

<section class="card card--back" aria-label="Business card, back">
  <svg class="card__shapes" viewBox="0 0 360 556" aria-hidden="true">
    <path d="M0 128 Q170 100 360 112 L360 318 Q210 332 0 392 Z" fill="var(--pink)"/>
    <path d="M0 136 Q180 108 360 120" fill="none" stroke="var(--white)" stroke-width="2"/>
    <line x1="30" y1="234" x2="330" y2="234" stroke="var(--white)" stroke-width="1.5"/>
    <path d="M0 404 Q170 350 360 330" fill="none" stroke="var(--pink)" stroke-width="3"/>
    <path d="M20 412 Q190 360 360 344" fill="none" stroke="var(--dark-gray)" stroke-width="1.2"/>
  </svg>
  <div class="social" style="top:14px">
    <div class="social__row"><span class="social__mark"></span>social.example/TarvelloConsulting</div>
    <div class="social__row"><span class="social__mark"></span>chirp.example/TarvelloConsulting</div>
  </div>
  <p class="tagline">Web Design &amp; Development Company in Brackwell</p>
  <p class="services">Graphic Design | S.E.O &amp; Marketing<br>Application Design</p>
  <div class="brand"><span class="brand__dot"></span><span class="brand__name">Tarvello Consulting</span></div>
  <p class="url">www.tarvelloexample.co.uk</p>
</section>

<section class="card card--front" aria-label="Business card, front">
  <svg class="card__shapes" viewBox="0 0 360 556" aria-hidden="true">
    <path d="M0 0 H360 V82 Q200 88 0 124 Z" fill="var(--black)"/>
    <path d="M0 132 Q200 94 360 92" fill="none" stroke="var(--black)" stroke-width="2"/>
    <path d="M0 556 V372 Q180 330 360 318 V556 Z" fill="var(--pink)"/>
    <path d="M0 362 Q180 320 360 308" fill="none" stroke="var(--pink)" stroke-width="2"/>
  </svg>
  <div class="brand"><span class="brand__dot"></span><span class="brand__name">Tarvello Consulting</span></div>
  <div class="person">
    <h1 class="person__name">Sam Carter</h1>
    <p class="person__role">Chief Executive Officer</p>
  </div>
  <ul class="contact contact--personal">
    <li><svg width="14" height="16" viewBox="0 0 14 16"><rect x="3" y="1" width="8" height="14" rx="1.5" fill="none" stroke="var(--dark-gray)" stroke-width="1.5"/><line x1="6" y1="12.5" x2="8" y2="12.5" stroke="var(--dark-gray)" stroke-width="1.5"/></svg>+441632960418</li>
    <li><svg width="14" height="16" viewBox="0 0 14 16"><rect x="0.75" y="3.75" width="12.5" height="8.5" fill="var(--dark-gray)"/><path d="M1 4 L7 9 L13 4" fill="none" stroke="var(--white)" stroke-width="1.2"/></svg>sam.carter@tarvelloexample.co.uk</li>
  </ul>
  <ul class="contact contact--company">
    <li><svg width="16" height="18" viewBox="0 0 16 18"><path d="M8 17 C3 11 2 9 2 6.5 A6 6 0 0 1 14 6.5 C14 9 13 11 8 17 Z" fill="var(--white)"/><circle cx="8" cy="6.5" r="2.2" fill="var(--pink)"/></svg><span>7 Ashlin Grove, Brackwell,<br>Westmere, ZX14 6JB</span></li>
    <li><svg width="16" height="18" viewBox="0 0 16 18"><path d="M3 2 L6 2 L7.5 6 L5.5 7.5 Q7 11 10.5 12.5 L12 10.5 L16 12 L16 15 Q15 17 12 16.5 Q3 14 1 4 Q1 2 3 2 Z" fill="var(--white)"/></svg>01632 960215</li>
    <li><svg width="16" height="18" viewBox="0 0 16 18"><rect x="0.75" y="4" width="14.5" height="10" fill="var(--white)"/><path d="M1 4.5 L8 10 L15 4.5" fill="none" stroke="var(--pink)" stroke-width="1.3"/></svg>info@tarvelloexample.co.uk</li>
    <li><svg width="16" height="18" viewBox="0 0 16 18"><circle cx="8" cy="9" r="7" fill="none" stroke="var(--white)" stroke-width="1.5"/><ellipse cx="8" cy="9" rx="3" ry="7" fill="none" stroke="var(--white)" stroke-width="1.2"/><line x1="1" y1="9" x2="15" y2="9" stroke="var(--white)" stroke-width="1.2"/></svg>www.tarvelloexample.co.uk</li>
  </ul>
</section>

</body>
</html>
```